2014 Programme

We need a brochure for some training courses we are providing.

All content is available: http://brixolab.com/academy/brixolab-academy-programmes-2014

The brochure should be delivered in PDF and will be printed at a later date.

```html
<!DOCTYPE html>
<html lang="en">
<head>
<meta charset="utf-8">
<title>Brixolab Academy 2014 Programme – Contacts</title>
<link href="https://fonts.googleapis.com/css2?family=Titillium+Web:wght@200;300;700&display=swap" rel="stylesheet">
<style>
  :root {
    --paper: #ffffff;
    --magenta: #dc1482;
    --purple: #821487;
    --aqua: #a6edf1;
    --ink: #3c3c3c;
    --ink-soft: #6a6a6a;
  }
  * { margin: 0; padding: 0; box-sizing: border-box; }
  html, body { width: 848px; height: 1200px; overflow: hidden; background: var(--paper); }
  .back-cover {
    position: relative;
    width: 848px;
    height: 1200px;
    overflow: hidden;
    background: var(--paper);
    font-family: "Titillium Web", sans-serif;
    color: var(--ink);
  }
  .cover-artwork {
    position: absolute;
    left: 0;
    top: 0;
    width: 848px;
    height: 920px;
    background: linear-gradient(160deg, var(--aqua) 0%, var(--magenta) 30%, var(--purple) 65%, var(--aqua) 100%);
  }
  .contacts { position: absolute; left: 52px; top: 954px; }
  .contacts-title {
    font-weight: 200;
    font-size: 37px;
    letter-spacing: 0.8px;
    line-height: 1;
    color: var(--ink);
    margin-bottom: 22px;
  }
  .offices { display: flex; }
  .office { width: 264px; }
  .office-name {
    font-weight: 700;
    font-size: 15.5px;
    letter-spacing: 0.4px;
    line-height: 20px;
    color: var(--ink);
  }
  .office-address, .contact-lines {
    font-style: normal;
    font-weight: 300;
    font-size: 15.5px;
    letter-spacing: 0.6px;
    line-height: 20px;
    text-transform: uppercase;
    color: var(--ink-soft);
  }
  .contact-lines { margin-top: 20px; }
</style>
</head>
<body>
<main class="back-cover">
  <div class="cover-artwork" role="img" aria-label="Flowing abstract wave artwork in magenta, purple and aqua"></div>

  <section class="contacts">
    <h1 class="contacts-title">CONTACTS</h1>
    <div class="offices">
      <div class="office">
        <h2 class="office-name">AUSTRALIA</h2>
        <address class="office-address">42 Harbourline Street<br>Redfern Vale NSW 2016<br>Australia</address>
        <address class="contact-lines">info@brixolab.com<br>+61 2 5550 4172</address>
      </div>
      <div class="office">
        <h2 class="office-name">SOUTHEAST ASIA</h2>
        <address class="office-address">Studio 9, Block 14<br>Kallang Bay Crescent #03-17<br>Singapore</address>
      </div>
    </div>
  </section>
</main>
</body>
</html>
```